"Here We Go" Dance Production Poster

This is a dance school annual theatre performance, at the Lanworth Guild Playhouse. The dates are from the 26th-28th July 2012, and the show is called "Here We Go."

Although not themed around Desmond Farrow specifically, we are using a few songs hence the title.

We need an eye catching poster with out focusing too much around DF. Maybe even using his theme/image subliminally but must look professional and vivid.

We are a dance school predominantly female based with a few males - age range 2-55
Updates

Hi guys - please check brief 

We are getting to many designs based too much around Desmond Farrow

This only has to be subliminal as the show isn't about him, it's mainly a generic dance show

Please try to bare this in mind

Thanks

Target Market(s)

Parents, family, friends of the performers/general public

Industry/Entity Type

School

Requirements
Must have
• The Hollis Brandt School Of Dance Present "Here We Go"
26th-28th July 2012 at the Lanworth Guild

Tickets available from the Theatre Box Office

www.hbschoolofdance-example.co.uk

Nice to have
• Subliminal Desmond Farrow feel - no pictures of him though
Should not have
• Cheap templates, poor images, flowery fonts

```html
<!DOCTYPE html>
<html lang="en">
<head>
<meta charset="utf-8">
<title>Here We Go — The Hollis Brandt School Of Dance</title>
<link rel="stylesheet" href="https://fonts.googleapis.com/css2?family=Playball&family=Source+Sans+3:wght@300&display=swap">
<style>
  :root {
    --ink-black: #050308;
    --glow-purple: #5a0a6e;
    --glow-mid: #2a0836;
    --accent-yellow: #efe13a;
    --title-white: #f7f0ff;
    --title-pink: #e9a6f2;
    --title-halo: #d58cff;
    --hand-light: rgba(228, 226, 230, 0.9);
    --hand-shade: rgba(141, 138, 146, 0.45);
  }
  * { margin: 0; padding: 0; box-sizing: border-box; }
  html, body {
    width: 848px;
    height: 1200px;
    overflow: hidden;
    background: var(--ink-black);
  }
  .poster {
    position: relative;
    width: 848px;
    height: 1200px;
    overflow: hidden;
    background:
      radial-gradient(ellipse 360px 420px at 424px 520px,
        var(--glow-purple) 0%, var(--glow-mid) 45%, var(--ink-black) 100%);
    font-family: "Source Sans 3", sans-serif;
    font-weight: 300;
    color: var(--accent-yellow);
  }
  .presenter {
    position: absolute;
    top: 186px;
    left: 0;
    width: 100%;
    text-align: center;
    font-size: 38px;
    line-height: 48px;
  }
  .show-title {
    position: absolute;
    top: 300px;
    left: 0;
    width: 100%;
    text-align: center;
    font-family: "Playball", cursive;
    font-weight: 400;
    font-size: 168px;
    line-height: 210px;
    color: var(--title-white);
    text-shadow:
      0 0 6px var(--title-pink),
      0 0 18px var(--title-halo),
      0 0 36px rgba(213, 140, 255, 0.55);
  }
  .show-title span { display: block; }
  .details {
    position: absolute;
    top: 730px;
    left: 0;
    width: 100%;
    text-align: center;
  }
  .details .dates { font-size: 39px; line-height: 50px; }
  .details .venue { font-size: 30px; line-height: 40px; }
  .details .tickets { font-size: 32px; line-height: 42px; margin-top: 14px; }
  .hand-photo {
    position: absolute;
    left: -40px;
    top: 940px;
    width: 400px;
    height: 320px;
    background: radial-gradient(ellipse 200px 170px at 45% 65%,
      var(--hand-light) 0%, var(--hand-shade) 55%, rgba(141,138,146,0) 100%);
  }
  .website {
    position: absolute;
    right: 16px;
    bottom: 18px;
    font-size: 23px;
  }
</style>
</head>
<body>
  <main class="poster">
    <p class="presenter">The Hollis Brandt School Of Dance Present:</p>
    <h1 class="show-title"><span>HERE</span><span>WE GO</span></h1>
    <section class="details">
      <p class="dates">26th - 28th July 2012</p>
      <p class="venue">at the Lanworth Guild</p>
      <p class="tickets">Tickets available from the Theatre Box Office</p>
    </section>
    <div class="hand-photo" role="img" aria-label="Photograph of a raised hand in a pale sparkly costume reaching up from the lower left corner"></div>
    <p class="website">www.hbschoolofdance-example.co.uk</p>
  </main>
</body>
</html>
```